Karvelin PowerPoint Templates

We need a cover page and body page templates for a complete Powerpoint presentation. We administer workers' compensation claims in California mostly to public entities. We offer cloud based software to develop and communicate all the data for each claim. Although we are a technology company, we also see ourselves as the human interface working closely with the client and injured workers.
It all starts with our Logo!
We want to loosely relate our Powerpoint design with our Logo. Maybe just in the color! WE DONT WANT TO RECREATE OUR LOGO AS A PROPOSAL . I've posted the logo and a rough proposal page for reference. We designed it using ArtHive and feel the designer met our criteria very well. As I recall the spec for the logo was to use our name and incorporate "modern, professional and personal" into the design. We will use this template to attract new business. We will be approaching a variety of industries and want the template to be designed specifically for our business identity rather than for clients we are pursuing.
I will also post a simple example of a competitor's PowerPoint presentation for reference.
Please feel free to ask any questions you may have.
Thank You!
Harold

```html
<!DOCTYPE html>
<html lang="en">
<head>
<meta charset="utf-8">
<title>Karvelin Presentation Template Set</title>
<link rel="stylesheet" href="https://fonts.googleapis.com/css2?family=Bebas+Neue&family=Open+Sans:wght@400;600;700&display=swap">
<style>
:root{
  --stage:#2b2c30;
  --blue:#2a5db0;
  --blue-dark:#1f4a91;
  --yellow:#f6c417;
  --charcoal:#4a4b4e;
  --grey:#9a9b9e;
  --grey-light:#c9cacc;
  --paper:#f4f4f5;
  --ink:#333436;
  --white:#ffffff;
}
*{box-sizing:border-box}
html,body{margin:0;padding:0;overflow:hidden}
body{width:1200px;height:1080px;background:var(--stage);position:relative;font-family:'Open Sans',Arial,sans-serif;color:var(--ink)}
.slide{position:absolute;width:338px;height:254px;background:var(--paper);overflow:hidden}
.abs{position:absolute}
.display{font-family:'Bebas Neue',Impact,sans-serif;font-weight:400;letter-spacing:.3px;margin:0}
.body-text{font-size:4.6px;line-height:6.2px;margin:0;color:var(--ink)}

/* brand name */
.brand{position:absolute;display:flex;align-items:center;gap:3px;color:var(--blue);font-family:'Open Sans',Arial,sans-serif;font-weight:700;white-space:nowrap}
.brand .dot{border-radius:50%;background:var(--blue)}
.tagline{position:absolute;color:var(--ink);font-weight:600;white-space:nowrap}

/* body page header and footer */
.hdr{position:absolute;left:0;top:0;width:338px;height:24px;background:var(--blue)}
.hdr h2{font-family:'Bebas Neue',Impact,sans-serif;font-weight:400;font-size:15px;line-height:25px;color:var(--white);margin:0 0 0 13px;letter-spacing:.4px}
.hdr .brand-cell{position:absolute;right:0;top:0;width:66px;height:24px;background:var(--white);clip-path:polygon(10px 0,100% 0,100% 100%,0 100%)}
.hdr .brand{right:6px;top:6px;font-size:9px}
.hdr .brand .dot{width:4px;height:4px}
.foot{position:absolute;left:0;bottom:0;width:338px;height:10px;background:var(--charcoal)}
.foot .copy{position:absolute;left:8px;top:2px;font-size:3.6px;color:var(--white)}
.foot .date-band{position:absolute;right:0;top:0;width:118px;height:10px;background:var(--blue);clip-path:polygon(8px 0,100% 0,100% 100%,0 100%)}
.foot .date{position:absolute;left:30px;top:2px;font-size:3.8px;color:var(--white);font-weight:600}
.foot .page{position:absolute;right:5px;top:2px;width:8px;height:6px;background:var(--white);color:var(--blue);font-size:3.4px;text-align:center;line-height:6px}

.photo{position:absolute;background:linear-gradient(160deg,#d6d8db,#8e949b 60%,#3d4552);border:1px solid #ccc}
.pattern{position:absolute;background:radial-gradient(ellipse at 60% 45%,rgba(150,150,150,.35),rgba(150,150,150,.08) 65%,rgba(150,150,150,0) 80%)}

/* slide placement */
.s-title-a{left:28px;top:16px;background:var(--white)}
.s-title-b{left:414px;top:16px}
.s-title-c{left:793px;top:16px;background:var(--white)}
.s-content{left:28px;top:288px}
.s-graphics{left:414px;top:288px}
.s-about{left:793px;top:288px}
.s-team{left:28px;top:550px}
.s-bars{left:414px;top:550px}
.s-donut{left:793px;top:550px}
.s-table{left:222px;top:816px}
.s-thanks{left:600px;top:816px}

/* services */
.service{position:absolute;top:70px;width:90px;text-align:center}
.service .badge{width:40px;height:40px;border-radius:50%;margin:0 auto;display:flex;align-items:center;justify-content:center}
.service h3{font-family:'Bebas Neue',Impact,sans-serif;font-weight:400;font-size:7px;margin:12px 0 3px;letter-spacing:.3px}

/* team */
.member{position:absolute;top:52px;width:84px;text-align:center}
.member .photo{position:relative;width:42px;height:50px;margin:0 auto}
.member .name{font-size:5.6px;font-weight:700;color:var(--blue);margin-top:4px}
.member .role{font-size:4.4px;color:var(--ink);margin-top:1px}
.member .rule{width:44px;height:3px;background:var(--blue);margin:6px auto 6px}

/* tables */
.grid{position:absolute;border-collapse:collapse;font-size:3.6px;table-layout:fixed}
.grid th{background:var(--blue);color:var(--white);font-weight:600;height:10px;border:0.5px solid var(--white);padding:0}
.grid td{height:8.6px;border:0.5px solid #d2d3d5;padding:0;text-align:center}
.grid.light td{background:var(--white)}
.grid.dark td{background:#7d7e81;border-color:#a5a6a8;color:var(--white)}
.grid-foot{position:absolute;height:9px;background:var(--charcoal)}

.legend{position:absolute;display:flex;align-items:center;gap:4px;font-size:4.4px}
.legend i{display:block;width:11px;height:11px;border-radius:50%}

.contact{position:absolute;left:12px;display:flex;align-items:center;gap:6px;font-size:4.8px;color:var(--blue)}
</style>
</head>
<body>

<!-- Title slide A -->
<section class="slide s-title-a">
  <div class="brand" style="right:18px;top:20px;font-size:18px;"><span class="dot" style="width:7px;height:7px"></span>Karvelin</div>
  <div class="tagline" style="right:22px;top:42px;font-size:4.6px">Claims Management Solutions</div>
  <svg class="abs" style="left:0;top:0" width="338" height="254" viewBox="0 0 338 254">
    <polygon points="0,72 92,72 100,84 0,84" fill="var(--grey-light)"/>
    <polygon points="0,84 250,84 262,96 338,96 338,180 0,180" fill="var(--blue)"/>
    <polygon points="110,180 310,180 330,198 130,198" fill="var(--grey-light)"/>
    <polygon points="130,180 170,180 192,198 152,198" fill="var(--charcoal)"/>
  </svg>
  <div class="abs" style="left:8px;top:74px;font-size:4.6px;color:var(--white)">Subtitle goes here</div>
  <h1 class="display abs" style="left:0;width:338px;top:118px;text-align:center;font-size:27px;color:var(--white)">Presentation Title</h1>
  <div class="abs" style="left:10px;bottom:6px;font-size:5px">PRESENTOR NAME</div>
  <div class="abs" style="right:12px;bottom:6px;font-size:5px">Dec 31 &nbsp;2014</div>
</section>

<!-- Title slide B -->
<section class="slide s-title-b">
  <div class="brand" style="left:104px;top:34px;font-size:26px;"><span class="dot" style="width:9px;height:9px"></span>Karvelin</div>
  <div class="tagline" style="left:108px;top:68px;font-size:6px">Claims Management Solutions</div>
  <div class="abs" style="left:0;top:102px;width:338px;height:152px;background:linear-gradient(180deg,#cfd0d2,#c3c4c6)"></div>
  <div class="pattern" role="img" aria-label="Connected dots network pattern" style="left:180px;top:112px;width:158px;height:130px"></div>
  <svg class="abs" style="left:0;top:0" width="338" height="254" viewBox="0 0 338 254">
    <polygon points="210,100 338,100 338,116 222,116" fill="var(--blue)"/>
    <line x1="12" y1="192" x2="140" y2="192" stroke="#666" stroke-width="0.8" stroke-dasharray="2 1.5"/>
    <circle cx="76" cy="192" r="4.5" fill="var(--paper)" stroke="#555" stroke-width="1.6"/>
  </svg>
  <div class="abs" style="left:234px;top:103px;font-size:5.6px;color:var(--white);font-weight:600">Subtitle goes here</div>
  <h1 class="display abs" style="left:14px;top:160px;font-size:23px;color:var(--blue)">Presentation Title</h1>
  <div class="abs" style="left:10px;bottom:5px;font-size:5px;color:var(--blue)">PRESENTOR NAME</div>
  <div class="abs" style="right:10px;bottom:5px;font-size:5px;color:var(--blue)">DEC 31 &nbsp;2014</div>
</section>

<!-- Title slide C -->
<section class="slide s-title-c">
  <div class="abs" style="left:14px;top:14px;width:3px;height:34px;background:var(--blue)"></div>
  <h1 class="display abs" style="left:22px;top:14px;font-size:19px;color:var(--blue)">Presentation Title</h1>
  <div class="abs" style="left:22px;top:36px;font-size:5.4px;color:var(--grey)">SUBTITLE GOES HERE</div>
  <div class="pattern" role="img" aria-label="Connected dots network pattern" style="left:110px;top:8px;width:228px;height:246px"></div>
  <div class="brand" style="left:18px;top:204px;font-size:13px;"><span class="dot" style="width:5px;height:5px"></span>Karvelin</div>
  <div class="tagline" style="left:20px;top:221px;font-size:4px">Claims Management Solutions</div>
</section>

<!-- Content page -->
<section class="slide s-content">
  <header class="hdr"><h2>Content Page</h2><div class="brand-cell"><div class="brand"><span class="dot"></span>Karvelin</div></div></header>
  <div class="display abs" style="left:52px;top:44px;font-size:22px;color:var(--ink)">&ldquo;</div>
  <h3 class="display abs" style="left:20px;top:66px;width:86px;text-align:center;font-size:11px;color:var(--blue)">Lorem Ipsum</h3>
  <p class="body-text abs" style="left:22px;top:80px;width:82px;text-align:center">Lorem Ipsum is simply dummy text of the printing and typesetting industry. Lorem Ipsum has been the industry's standard dummy text ever since the 1500s, when an unknown printer took a galley of type and scrambled it to make a type specimen book. Lorem Ipsum is simply dummy text of the printing and typesetting industry.</p>
  <div class="display abs" style="left:52px;top:188px;font-size:22px;color:var(--ink)">&rdquo;</div>
  <div class="abs" style="left:120px;top:66px;width:2px;height:144px;background:var(--ink)"></div>
  <h3 class="display abs" style="left:132px;top:52px;font-size:9.5px;color:var(--blue)">Lorem Ipsum Consectetur Adipiscing Elit</h3>
  <p class="body-text abs" style="left:132px;top:66px;width:194px">It is a long established fact that a reader will be distracted by the readable content of a page when looking at its layout. The point of using Lorem Ipsum is that it has a more or less normal distribution of letters, as opposed to using 'Content here, content here', making it look like readable English. Many desktop publishing packages and web page editors now use Lorem Ipsum as their default model text, and a search for 'lorem ipsum' will uncover many web sites still in their infancy. Various versions have evolved over the years, sometimes by accident, sometimes on purpose.</p>
  <p class="body-text abs" style="left:132px;top:140px;width:194px">It is a long established fact that a reader will be distracted by the readable content of a page when looking at its layout. The point of using Lorem Ipsum is that it has a more or less normal distribution of letters, as opposed to using 'Content here, content here', making it look like readable English. Many desktop publishing packages and web page editors now use Lorem Ipsum as their default model text.</p>
  <footer class="foot"><span class="copy">Copyrights information</span><div class="date-band"><span class="date">DEC 31 &nbsp;2014</span></div><span class="page">02</span></footer>
</section>

<!-- Content graphics -->
<section class="slide s-graphics">
  <header class="hdr"><h2>Content Graphics</h2><div class="brand-cell"><div class="brand"><span class="dot"></span>Karvelin</div></div></header>
  <div class="service" style="left:18px">
    <div class="badge" style="background:var(--blue)"><svg width="20" height="20" viewBox="0 0 20 20"><circle cx="10" cy="10" r="8" fill="none" stroke="#fff" stroke-width="1.4"/><circle cx="10" cy="10" r="3" fill="none" stroke="#fff" stroke-width="1.4"/><circle cx="10" cy="10" r="1" fill="#fff"/></svg></div>
    <h3 style="color:var(--blue)">Our Services</h3>
    <p class="body-text">Lorem Ipsum is simply dummy text of the printing and typesetting industry. Lorem Ipsum has been the industry's standard dummy text</p>
  </div>
  <div class="service" style="left:124px">
    <div class="badge" style="background:var(--yellow)"><svg width="20" height="20" viewBox="0 0 20 20"><rect x="3" y="3" width="14" height="14" fill="none" stroke="#fff" stroke-width="1.4"/><rect x="6" y="11" width="2" height="4" fill="#fff"/><rect x="9" y="8" width="2" height="7" fill="#fff"/><rect x="12" y="6" width="2" height="9" fill="#fff"/></svg></div>
    <h3 style="color:var(--yellow)">Our Services</h3>
    <p class="body-text">Lorem Ipsum is simply dummy text of the printing and typesetting industry. Lorem Ipsum has been the industry's standard dummy text</p>
  </div>
  <div class="service" style="left:230px">
    <div class="badge" style="background:var(--charcoal)"><svg width="20" height="20" viewBox="0 0 20 20"><rect x="3" y="4" width="14" height="10" fill="none" stroke="#fff" stroke-width="1.4"/><path d="M6 11 Q10 6 14 11" fill="none" stroke="#fff" stroke-width="1.2"/><rect x="7" y="15" width="6" height="1.5" fill="#fff"/></svg></div>
    <h3 style="color:var(--ink)">Our Services</h3>
    <p class="body-text">Lorem Ipsum is simply dummy text of the printing and typesetting industry. Lorem Ipsum has been the industry's standard dummy text</p>
  </div>
  <footer class="foot"><span class="copy">Copyrights information</span><div class="date-band"><span class="date">DEC 31 &nbsp;2014</span></div><span class="page">03</span></footer>
</section>

<!-- About us -->
<section class="slide s-about">
  <header class="hdr"><h2>About Us</h2><div class="brand-cell"><div class="brand"><span class="dot"></span>Karvelin</div></div></header>
  <div class="photo" role="img" aria-label="Portrait photo of a team leader" style="left:14px;top:52px;width:56px;height:68px"></div>
  <div class="abs" style="left:14px;top:128px;display:flex;flex-direction:column;gap:6px;font-size:4.8px">
    <div style="display:flex;align-items:center;gap:5px"><span style="width:7px;height:7px;border-radius:50%;background:var(--ink)"></span>Follow us on Chirpline</div>
    <div style="display:flex;align-items:center;gap:5px"><span style="width:7px;height:7px;border-radius:50%;background:var(--ink)"></span>Follow us on FaceLedger</div>
    <div style="display:flex;align-items:center;gap:5px"><span style="width:7px;height:7px;border-radius:50%;background:var(--ink)"></span>Connect on ProLink</div>
  </div>
  <h3 class="display abs" style="left:100px;top:52px;font-size:12px;color:var(--blue)">Name Here</h3>
  <div class="abs" style="left:100px;top:64px;font-size:5px;color:var(--ink)">LOREM IPSUM</div>
  <p class="body-text abs" style="left:100px;top:74px;width:226px">Lorem Ipsum is simply dummy text of the printing and typesetting industry. Lorem Ipsum has been the industry's standard dummy text ever since the 1500s, when an unknown printer took a galley of type and scrambled it to make a type specimen book. Lorem Ipsum is simply dummy text of the printing and typesetting industry. Lorem Ipsum has been the industry's standard dummy text ever since the 1500s, when an unknown printer took a galley of type and scrambled it to make a type specimen book. Lorem Ipsum is simply dummy text of the printing and typesetting industry. Lorem Ipsum has been the industry's standard dummy text ever since the 1500s, when an unknown printer took a galley of type and scrambled it to make a type specimen book.</p>
  <footer class="foot"><span class="copy">Copyrights information</span><div class="date-band"><span class="date">DEC 31 &nbsp;2014</span></div><span class="page">04</span></footer>
</section>

<!-- Our team -->
<section class="slide s-team">
  <header class="hdr"><h2>Our Team</h2><div class="brand-cell"><div class="brand"><span class="dot"></span>Karvelin</div></div></header>
  <div class="member" style="left:18px"><div class="photo" role="img" aria-label="Team member portrait photo"></div><div class="name">Name Goes Here</div><div class="role">Designation</div><div class="rule"></div><p class="body-text">Lorem Ipsum is simply dummy text of the printing and typesetting industry. Lorem Ipsum has been the industry's standard dummy text</p></div>
  <div class="member" style="left:127px"><div class="photo" role="img" aria-label="Team member portrait photo"></div><div class="name">Name Goes Here</div><div class="role">Designation</div><div class="rule"></div><p class="body-text">Lorem Ipsum is simply dummy text of the printing and typesetting industry. Lorem Ipsum has been the industry's standard dummy text</p></div>
  <div class="member" style="left:236px"><div class="photo" role="img" aria-label="Team member portrait photo"></div><div class="name">Name Goes Here</div><div class="role">Designation</div><div class="rule"></div><p class="body-text">Lorem Ipsum is simply dummy text of the printing and typesetting industry. Lorem Ipsum has been the industry's standard dummy text</p></div>
  <footer class="foot"><span class="copy">Copyrights information</span><div class="date-band"><span class="date">DEC 31 &nbsp;2014</span></div><span class="page">05</span></footer>
</section>

<!-- Bar chart -->
<section class="slide s-bars">
  <header class="hdr"><h2>Graphics Chart</h2><div class="brand-cell"><div class="brand"><span class="dot"></span>Karvelin</div></div></header>
  <h3 class="display abs" style="left:58px;top:46px;font-size:11px;color:var(--blue)">Chart Title</h3>
  <svg class="abs" style="left:14px;top:72px" width="140" height="100" viewBox="0 0 140 100" font-family="Open Sans, sans-serif" font-size="3.6" fill="#444">
    <g stroke="#ddd" stroke-width="0.4">
      <line x1="18" y1="4" x2="136" y2="4"/><line x1="18" y1="20" x2="136" y2="20"/><line x1="18" y1="36" x2="136" y2="36"/><line x1="18" y1="52" x2="136" y2="52"/><line x1="18" y1="68" x2="136" y2="68"/>
    </g>
    <line x1="18" y1="84" x2="136" y2="84" stroke="#999" stroke-width="0.6"/>
    <text x="3" y="5.5">25.0%</text><text x="3" y="21.5">20.0%</text><text x="3" y="37.5">15.0%</text><text x="3" y="53.5">10.0%</text><text x="4" y="69.5">5.0%</text><text x="4" y="85.5">0.0%</text>
    <rect x="22" y="19" width="10" height="65" fill="var(--blue)"/><rect x="33" y="10" width="10" height="74" fill="var(--charcoal)"/>
    <rect x="47" y="45" width="10" height="39" fill="var(--blue)"/><rect x="58" y="55" width="10" height="29" fill="var(--charcoal)"/>
    <rect x="72" y="54" width="10" height="30" fill="var(--blue)"/><rect x="83" y="63" width="10" height="21" fill="var(--charcoal)"/>
    <rect x="97" y="62" width="10" height="22" fill="var(--blue)"/><rect x="108" y="65" width="10" height="19" fill="var(--charcoal)"/>
    <rect x="120" y="67" width="7" height="17" fill="var(--blue)"/><rect x="128" y="70" width="7" height="14" fill="var(--charcoal)"/>
    <text x="28" y="91">1 yr</text><text x="53" y="91">2 yr</text><text x="78" y="91">3 yr</text><text x="103" y="91">4 yr</text><text x="123" y="91">5 yr</text>
  </svg>
  <div class="legend" style="left:28px;top:186px"><i style="background:var(--blue)"></i>LOREM IPSUM</div>
  <div class="legend" style="left:92px;top:186px"><i style="background:var(--charcoal)"></i>LOREM IPSUM</div>
  <h3 class="display abs" style="left:190px;top:46px;font-size:11px;color:var(--blue)">Lorem Ipsum</h3>
  <p class="body-text abs" style="left:190px;top:62px;width:136px">Lorem Ipsum is simply dummy text of the printing and typesetting industry. Lorem Ipsum has been the industry's standard dummy text ever since the 1500s.</p>
  <p class="body-text abs" style="left:190px;top:98px;width:136px">when an unknown printer took a galley of type and scrambled it to make a type specimen book. Lorem Ipsum is simply dummy text of the printing and typesetting industry. Lorem Ipsum has been the industry's standard dummy text ever since the 1500s, when an unknown printer took a galley of type and scrambled it to make a type specimen book.</p>
  <p class="body-text abs" style="left:190px;top:164px;width:136px">Lorem Ipsum is simply dummy text of the printing and typesetting industry Lorem Ipsum is simply dummy text of the printing and typesetting industry.</p>
  <footer class="foot"><span class="copy">Copyrights information</span><div class="date-band"><span class="date">DEC 31 &nbsp;2014</span></div><span class="page">06</span></footer>
</section>

<!-- Donut chart -->
<section class="slide s-donut">
  <header class="hdr"><h2>Graphics Chart</h2><div class="brand-cell"><div class="brand"><span class="dot"></span>Karvelin</div></div></header>
  <h3 class="display abs" style="left:58px;top:46px;font-size:11px;color:var(--blue)">Chart Title</h3>
  <svg class="abs" style="left:14px;top:64px" width="140" height="110" viewBox="0 0 140 110" font-family="Open Sans, sans-serif" font-size="4.2" fill="#444">
    <g transform="rotate(-90 70 55)" fill="none" stroke-width="15">
      <circle cx="70" cy="55" r="36" stroke="var(--charcoal)" stroke-dasharray="113.1 226.2" stroke-dashoffset="0"/>
      <circle cx="70" cy="55" r="36" stroke="var(--blue)" stroke-dasharray="18.1 226.2" stroke-dashoffset="-113.1"/>
      <circle cx="70" cy="55" r="36" stroke="var(--yellow)" stroke-dasharray="20.4 226.2" stroke-dashoffset="-131.2"/>
      <circle cx="70" cy="55" r="36" stroke="var(--grey-light)" stroke-dasharray="74.6 226.2" stroke-dashoffset="-151.6"/>
    </g>
    <line x1="112" y1="42" x2="104" y2="46" stroke="#777" stroke-width="0.4"/><text x="113" y="42">50%</text>
    <line x1="98" y1="93" x2="88" y2="88" stroke="#777" stroke-width="0.4"/><text x="99" y="95">8%</text>
    <line x1="24" y1="88" x2="36" y2="78" stroke="#777" stroke-width="0.4"/><text x="16" y="91">9%</text>
    <line x1="26" y1="16" x2="40" y2="28" stroke="#777" stroke-width="0.4"/><text x="16" y="15">33%</text>
  </svg>
  <div class="legend" style="left:28px;top:186px"><i style="background:var(--blue)"></i>LOREM IPSUM</div>
  <div class="legend" style="left:100px;top:186px"><i style="background:var(--charcoal)"></i>LOREM IPSUM</div>
  <h3 class="display abs" style="left:190px;top:46px;font-size:11px;color:var(--blue)">Lorem Ipsum</h3>
  <p class="body-text abs" style="left:190px;top:62px;width:136px">Lorem Ipsum is simply dummy text of the printing and typesetting industry. Lorem Ipsum has been the industry's standard dummy text ever since the 1500s.</p>
  <p class="body-text abs" style="left:190px;top:98px;width:136px">when an unknown printer took a galley of type and scrambled it to make a type specimen book. Lorem Ipsum is simply dummy text of the printing and typesetting industry. Lorem Ipsum has been the industry's standard dummy text ever since the 1500s, when an unknown printer took a galley of type and scrambled it to make a type specimen book.</p>
  <p class="body-text abs" style="left:190px;top:164px;width:136px">Lorem Ipsum is simply dummy text of the printing and typesetting industry Lorem Ipsum is simply dummy text of the printing and typesetting industry.</p>
  <footer class="foot"><span class="copy">Copyrights information</span><div class="date-band"><span class="date">DEC 31 &nbsp;2014</span></div><span class="page">07</span></footer>
</section>

<!-- Table -->
<section class="slide s-table">
  <header class="hdr"><h2>Table</h2><div class="brand-cell"><div class="brand"><span class="dot"></span>Karvelin</div></div></header>
  <h3 class="display abs" style="left:15px;top:56px;font-size:9.5px;color:var(--ink)"><span style="color:var(--blue)">Light</span> Theme</h3>
  <h3 class="display abs" style="left:176px;top:56px;font-size:9.5px;color:var(--ink)"><span style="color:var(--blue)">Dark</span> Theme</h3>
  <table class="grid light" style="left:15px;top:70px;width:152px">
    <colgroup><col style="width:26px"><col><col><col></colgroup>
    <tr><th>S. No.</th><th>Lorem Ipsum</th><th>Lorem Ipsum</th><th>Lorem Ipsum</th></tr>
    <tr><td>1</td><td></td><td></td><td></td></tr><tr><td>2</td><td></td><td></td><td></td></tr><tr><td>3</td><td></td><td></td><td></td></tr><tr><td>4</td><td></td><td></td><td></td></tr><tr><td>5</td><td></td><td></td><td></td></tr><tr><td>6</td><td></td><td></td><td></td></tr><tr><td>7</td><td></td><td></td><td></td></tr><tr><td>8</td><td></td><td></td><td></td></tr><tr><td>9</td><td></td><td></td><td></td></tr><tr><td>10</td><td></td><td></td><td></td></tr><tr><td>11</td><td></td><td></td><td></td></tr>
  </table>
  <div class="grid-foot" style="left:15px;top:176px;width:152px"></div>
  <table class="grid dark" style="left:176px;top:70px;width:152px">
    <colgroup><col style="width:26px"><col><col><col></colgroup>
    <tr><th>S. No.</th><th>Lorem Ipsum</th><th>Lorem Ipsum</th><th>Lorem Ipsum</th></tr>
    <tr><td>1</td><td></td><td></td><td></td></tr><tr><td>2</td><td></td><td></td><td></td></tr><tr><td>3</td><td></td><td></td><td></td></tr><tr><td>4</td><td></td><td></td><td></td></tr><tr><td>5</td><td></td><td></td><td></td></tr><tr><td>6</td><td></td><td></td><td></td></tr><tr><td>7</td><td></td><td></td><td></td></tr><tr><td>8</td><td></td><td></td><td></td></tr><tr><td>9</td><td></td><td></td><td></td></tr><tr><td>10</td><td></td><td></td><td></td></tr><tr><td>11</td><td></td><td></td><td></td></tr>
  </table>
  <div class="grid-foot" style="left:176px;top:176px;width:152px"></div>
  <footer class="foot"><span class="copy">Copyrights information</span><div class="date-band"><span class="date">DEC 31 &nbsp;2014</span></div><span class="page">08</span></footer>
</section>

<!-- Thank you -->
<section class="slide s-thanks">
  <div class="brand" style="left:104px;top:30px;font-size:26px;"><span class="dot" style="width:9px;height:9px"></span>Karvelin</div>
  <div class="tagline" style="left:108px;top:64px;font-size:6px">Claims Management Solutions</div>
  <div class="abs" style="left:0;top:94px;width:338px;height:160px;background:linear-gradient(180deg,#d3d4d6,#c6c7c9)"></div>
  <div class="pattern" role="img" aria-label="Connected dots network pattern" style="left:170px;top:104px;width:168px;height:140px"></div>
  <svg class="abs" style="left:0;top:0" width="338" height="254" viewBox="0 0 338 254">
    <rect x="0" y="92" width="338" height="2.4" fill="var(--blue)"/>
    <polygon points="10,94 22,94 16,102" fill="var(--blue)"/>
    <line x1="12" y1="130" x2="150" y2="130" stroke="#888" stroke-width="0.5"/>
  </svg>
  <h2 class="display abs" style="left:12px;top:104px;font-size:25px;letter-spacing:3px;color:var(--blue)">Thank You</h2>
  <div class="contact" style="top:138px"><svg width="8" height="8" viewBox="0 0 10 10"><circle cx="5" cy="5" r="5" fill="var(--blue)"/><path d="M5 2.2a1.8 1.8 0 0 1 1.8 1.8C6.8 5.4 5 7.8 5 7.8S3.2 5.4 3.2 4A1.8 1.8 0 0 1 5 2.2z" fill="#fff"/></svg><span>Find Us<br>Address</span></div>
  <div class="contact" style="top:160px"><svg width="8" height="8" viewBox="0 0 10 10"><path d="M2 1.5l2 0 .8 2-1.2.8a5 5 0 0 0 2.1 2.1l.8-1.2 2 .8v2c-4 .4-7-2.6-6.5-6.5z" fill="var(--blue)"/></svg><span>000-000-0000</span></div>
  <div class="contact" style="top:176px"><svg width="8" height="8" viewBox="0 0 10 10"><rect x="1" y="2.5" width="8" height="5.5" fill="var(--blue)"/><path d="M1 2.5l4 3 4-3" fill="none" stroke="#fff" stroke-width="0.7"/></svg><span>hello@karvelin-mail.com</span></div>
  <div class="contact" style="top:192px"><svg width="8" height="8" viewBox="0 0 10 10"><circle cx="5" cy="5" r="4" fill="none" stroke="var(--blue)" stroke-width="1"/><ellipse cx="5" cy="5" rx="1.8" ry="4" fill="none" stroke="var(--blue)" stroke-width="0.7"/><line x1="1" y1="5" x2="9" y2="5" stroke="var(--blue)" stroke-width="0.7"/></svg><span>www.karvelin-claims.com</span></div>
  <div class="abs" style="right:38px;bottom:8px;width:8px;height:8px;background:var(--charcoal)"></div>
  <div class="abs" style="right:24px;bottom:8px;width:8px;height:8px;background:var(--charcoal)"></div>
  <div class="abs" style="right:10px;bottom:8px;width:8px;height:8px;background:var(--charcoal)"></div>
</section>

</body>
</html>
```